we are an outdoor outlet in a country club that has a variety of outlets. The Club is called Larkvale and is located in Cairo, Egypt. This garden menu will include cuisines from the Mediterranean, Asia and Texmex. we need a menu that is colorful and would fit an A3 size, back and front are to be used. Attached is the old menu currently in use (Garden Menu 2012.pdf is just for reference) and the new menu text for you to use is under the name Garden Menu Fall 2013
thank you.

```html
<!DOCTYPE html>
<html lang="en">
<head>
<meta charset="utf-8">
<title>Garden Menu – Larkvale Country Club</title>
<link href="https://fonts.googleapis.com/css2?family=Montserrat:wght@700&family=Arimo:wght@400;700&display=swap" rel="stylesheet">
<style>
:root{
  --green-dark:#0d5420;
  --lime:#b3d235;
  --mint:#c8e5cc;
  --gold:#c8881c;
  --sand:#fee8a5;
  --brown:#5a2a08;
  --ink:#3b3226;
  --white:#ffffff;
}
*{margin:0;padding:0;box-sizing:border-box}
html,body{width:1200px;height:849px;overflow:hidden;background:var(--white)}
.menu{position:relative;width:1200px;height:849px;font-family:"Arimo",Arial,sans-serif;font-size:12px;line-height:16.1px;color:var(--ink)}
.abs{position:absolute}

.title{left:380px;top:8px;font-family:"Montserrat",sans-serif;font-weight:700;font-size:56px;line-height:70px;color:var(--green-dark);letter-spacing:0.5px;white-space:nowrap}
.brand{left:955px;top:54px;display:flex;align-items:center;gap:10px;font-family:"Arimo",sans-serif;font-size:27px;line-height:34px;color:var(--gold);font-weight:400}
.brand-dot{width:38px;height:38px;border-radius:50%;background:var(--lime)}

.pill{background:var(--green-dark);color:var(--lime);font-family:"Arimo",sans-serif;font-weight:700;border-radius:10px;display:flex;align-items:center;justify-content:center;white-space:nowrap}
.pill-med{left:22px;top:91px;width:293px;height:39px;font-size:23px}
.pill-asia{left:370px;top:84px;width:430px;height:40px;font-size:26px}

.panel-med{left:8px;top:140px;width:337px;height:709px;background:var(--mint)}
.band-gold{left:8px;top:140px;width:335px;height:47px;background:var(--gold);color:var(--white);font-weight:700;font-size:24px;line-height:47px;padding-left:55px}
.price-strip{background:var(--white)}
.strip-med{left:272px;top:197px;width:66px;height:600px}

.panel-east{left:366px;top:135px;width:834px;height:714px;background:var(--sand)}
.band-east{left:366px;top:135px;width:834px;height:52px;background:var(--green-dark);border-radius:14px 14px 0 0}
.band-head{color:var(--white);font-weight:700;font-size:23px;line-height:24px;white-space:nowrap}
.head-asia{left:395px;top:157px}
.head-tex{left:780px;top:157px}
.tex-label{left:888px;top:131px;color:var(--lime);font-weight:700;font-size:25px;line-height:26px}
.strip-asia{left:680px;top:195px;width:31px;height:443px}
.strip-tex1{left:1128px;top:195px;width:60px;height:302px}
.strip-tex2{left:1128px;top:553px;width:60px;height:229px}

.col{position:absolute}
.col-med{left:8px;top:197px;width:330px}
.col-asia{left:379px;top:193px;width:332px}
.col-tex{left:729px;top:193px;width:459px}
.item-bar{display:flex;justify-content:space-between;background:var(--brown);color:var(--white);font-weight:700;height:15px;line-height:15px;padding:0 4px 0 8px;margin-bottom:1px;white-space:nowrap}
.col-asia .item-bar,.col-tex .item-bar{padding-left:4px}
.desc{padding-left:8px;width:266px;text-align:justify}
.col-asia .desc{padding-left:4px;width:257px}
.col-tex .desc{padding-left:4px;width:378px;text-align:left}
.desc-left{text-align:left !important}
.subhead{font-weight:700;padding-left:8px}
.col-asia .subhead,.col-tex .subhead{padding-left:4px}

.pill-dessert{left:731px;top:523px;width:469px;height:30px;background:var(--green-dark);border-radius:12px 0 0 12px;color:var(--white);font-weight:700;font-size:22px;line-height:30px;padding-left:60px}
.dessert-list{left:733px;top:563px;list-style:none;line-height:16.2px}

.photo-salad{left:413px;top:645px;width:228px;height:202px;background:radial-gradient(circle at 50% 45%,#7e5d84 0%,#6b6f90 35%,#8fbf4c 70%,#e9e9e6 100%)}
.photo-brulee{left:969px;top:561px;width:122px;height:122px;border-radius:50%;background:radial-gradient(circle at 50% 45%,#d28f2a 0%,#e9e0d4 55%,#b0372e 100%)}
</style>
</head>
<body>
<div class="menu">
  <h1 class="abs title">GARDEN MENU</h1>
  <div class="abs brand"><span class="brand-dot"></span>Larkvale</div>

  <div class="abs pill pill-med">Mediterranean Corner</div>
  <div class="abs pill pill-asia">Asian Corner</div>

  <div class="abs panel-med"></div>
  <div class="abs band-gold">Pizza &amp; Pasta:</div>
  <div class="abs price-strip strip-med"></div>

  <div class="abs panel-east"></div>
  <div class="abs band-east"></div>
  <div class="abs tex-label">Tex Mex</div>
  <div class="abs band-head head-asia">Salads &amp; Appetizers:</div>
  <div class="abs band-head head-tex">Salads &amp; Appetizers:</div>
  <div class="abs price-strip strip-asia"></div>
  <div class="abs price-strip strip-tex1"></div>
  <div class="abs price-strip strip-tex2"></div>

  <section class="col col-med">
    <div class="item-bar"><span>Pizza Margarita</span><span>L.E 34.00</span></div>
    <p class="desc desc-left">(Choose your toppings)<br>Create your own pasta</p>
    <div class="item-bar"><span>Type:Spaghetti, Tagliatelle, Penne</span></div>
    <p class="desc desc-left">Sauces: Napolitana, Bolognese, Alfredo<br>Toppings:<br>Bell peppers, olives, tomato, onion<br>Mushroom, chicken, tuna, pepperoni<br>Smoked salmon, shrimps<br>Lasagna</p>
    <div class="item-bar"><span>Sandwiches:</span></div>
    <p class="desc desc-left">(Served with French fries or a garden<br>salad)<br>Beef or chicken Shawerma<br>Grilled kofta<br>Greek lamb gyro in pita bread with<br>Tzatziki<br>Club sandwichwith smoked beef, turkey, egg</p>
    <p class="subhead">Main Courses:</p>
    <div class="item-bar"><span>Veal Parmeggiana</span></div>
    <p class="desc">Breaded veal escalope topped with melted cheese and tomato sauce served with Spa-ghetti</p>
    <div class="item-bar"><span>Chicken a la Francaise</span></div>
    <p class="desc">Pan fried chicken breast in a mushroom cream sauce with vegetables white rice</p>
    <div class="item-bar"><span>Grilled Salmon</span></div>
    <p class="desc">Salmon steak charcoal grilled with avocado to-mato relish and creamy mushroom risotto</p>
    <div class="item-bar"><span>Moroccan Chicken</span></div>
    <p class="desc">Chicken cubes simmered with spices and ol-ives served with tomato rice</p>
    <div class="item-bar"><span>Filet</span></div>
    <p class="desc">Tender filet grilled to your liking served with mashed potato and creamed spinach</p>
    <p class="desc">Choice of sauces: Brown mushroom, Green Peppercorn, Gorgonzola</p>
  </section>

  <section class="col col-asia">
    <div class="item-bar"><span>Chicken Wasabi Salad</span></div>
    <p class="desc">Diced chicken with a mayo wasabi dressing on top of shredded lettuce</p>
    <div class="item-bar"><span>Chicken Sesame Noodle Salad</span></div>
    <p class="desc">Sesame crusted chicken with glass noodles tossed with sweet chili, soy sauce, and lem-ongrass</p>
    <div class="item-bar"><span>Spring rolls</span></div>
    <p class="desc desc-left">Vegetable spring rolls served with house made sweet and sour dip</p>
    <div class="item-bar"><span>Indian Samosa</span></div>
    <p class="desc desc-left">Fried dough parcels filled with vegetables and spices</p>
    <p class="subhead">Main Courses:</p>
    <div class="item-bar"><span>Murgh Chicken Makhni</span></div>
    <p class="desc desc-left">Chicken cubes in a rich creamy tomato sauce seasoned with garam masala</p>
    <p class="desc desc-left">Choice of side: vegetable korma or curd</p>
    <div class="item-bar"><span>Chicken Tandoori</span></div>
    <p class="desc">Grilled chicken cubes with tandoori spices served with basmati rice</p>
    <div class="item-bar"><span>Thai Coconut Curry Shrimp</span></div>
    <p class="desc desc-left">Sautéed shrimp tossed with curry and coconut milk served with jasmine rice</p>
    <div class="item-bar"><span>Mongolian Beef</span></div>
    <p class="desc desc-left">Soy marinated beef with oyster sauce and veg-etables served with egg noodles</p>
  </section>

  <section class="col col-tex">
    <div class="item-bar"><span>Caesar Salad</span></div>
    <p class="desc">Iceberg lettuce with Caesar dressing with grated Parmesan cheese and croutons</p>
    <div class="item-bar"><span>Taco salad42</span></div>
    <p class="desc">Chicken breast, beans, sour cream, guacamole, tomato, corn, lettuce, olives, chives, vinaigrette<br>Nachos topped with chili, melted cheese, beans<br>Chicken Quesadilla served with guacamole, salsa, and sour cream</p>
    <p class="subhead">Main Courses &amp; Sandwiches:</p>
    <div class="item-bar"><span>Cheeseburger</span></div>
    <p class="desc">House made lean beef burger topped with cheddar cheese</p>
    <div class="item-bar"><span>Mushroom Burger</span></div>
    <p class="desc">Beef burger with sautéed mushroom, caramelized onion, and provolone cheese</p>
    <div class="item-bar"><span>Crispy Chicken Wrap</span></div>
    <p class="desc">Crisp fried chicken wrap with a ranch dressing<br>Fajita (Chicken, Beef, Combo)<br>Pan seared meat or chicken with onion and bell pepper served with sour cream, guacamole, salsa</p>
  </section>

  <div class="abs pill-dessert">Desserts</div>
  <ul class="abs dessert-list">
    <li>Mix Berries Cheesecake</li>
    <li>Crème Brulee</li>
    <li>Chocolate Caramel Cake</li>
    <li>Warm Chocolate Fondant</li>
    <li>Baked Apple Tart Tatin</li>
    <li>Tiramisu</li>
    <li>Pumpkin Pie Flan</li>
    <li>Mixed Berries Granola Yoghurt</li>
    <li>Vanilla Ice Cream Profiterole with dark and white chocolate sauce</li>
    <li>Caramelized Banana with Deep Fried Ice Cream</li>
    <li>Baklava with Nuts and Sugar Syrup</li>
    <li>Shot Glass Sampler – Tiramisu, Chocolate Crisp Mousse, Pear with<br>Sabayon</li>
    <li>Ice Cream by Scoop</li>
  </ul>

  <div class="abs photo-salad" role="img" aria-label="Photo of a bowl of chopped potatoes, red onion, green pepper and spring onion"></div>
  <div class="abs photo-brulee" role="img" aria-label="Round photo of crème brulée ramekins on a red cloth"></div>
</div>
</body>
</html>
```